New Consumer Electronics online shop needs logo & web design

Background:

I'm a web developer who needs a designer for this task. I can do some simple design + UX and back-end programming, so you need to be a gun designer. If you can also cut-up, it's a bonus, but I need someone who understands and breathes design, not interested in a hack design job.

The Job:

I need

(1) a logo for "plovy" (plovy.example and plovy.example.au) pronounced "plo-vee". (the logo is going to be more "fun" looking than the web site)
(2) a simple, clean and elegant web design for an online shop

plovy is an online shop that sells top-line consumer electronic products at heavily discounted prices: think Quorra laptops, kPods, kSlates, Velmori smartphones, SLR or high-end compact Cameras and lenses.

The feel for this business is contemporary, simple, affordable (but not cheap), and someone who understands the technology, and only sells the best brands and latest items.

The web site and web shop is customised (not pagecraft) but should be not too colourful (think quorra products, platinum, white, black, grey, or SLR cameras, etc) though sparse use of colour is ok.

Basically the final site should convey the products themselves (and their qualities)

Deliverables:

1) Logo, in AI and PNG
2) Web site, in PSD format ready for cut-up. Provide (a) home page design + (b) product page + (c) general "blank" content page (for putting content/ordering/cart, etc). provide sample layer for nav widget.

Criteria:
* good design
* cut-up to CSS/JS/HTML a bonus to win, but if you can't do cut up, just do more 1-2 more PSD samples of the web site.
* basically, the best/good enough design that needs me to do the least work wins! :)

It's a dead easy job for a good designer!
Updates

Sorry if you missed this, but submissions are looking a lot like modified PageCraft templates.

The target platform is not PageCraft.

If you can distinguish yourself from the crowd it would be to your advantage.

Target Market(s)

People looking for top brand electronic goods in a brand they can trust at a price that is (around) 2nd-3rd cheapest.

Industry/Entity Type

Business

Requirements
Must have
• Should be showcasing products. The site does not have many products initially - maybe up to 50.

Needs to be uncluttered.
Should not have
• no cartoon characters.
not too boring - not corporate.

```html
<!DOCTYPE html>
<html lang="en">
<head>
<meta charset="utf-8">
<title>plovy – Register</title>
<link href="https://fonts.googleapis.com/css2?family=PT+Sans:wght@400;700&display=swap" rel="stylesheet">
<style>
:root{
  --header:#3a3a3a;
  --header-dark:#333;
  --tab:#555;
  --red:#d0191c;
  --text:#555;
  --label:#555;
  --field:#efefef;
  --field-line:#dcdcdc;
  --rule:#e2e2e2;
  --footer:#333;
  --footer-bar:#555;
  --footer-text:#ddd;
  --white:#fff;
}
*{box-sizing:border-box;margin:0;padding:0}
html,body{width:966px;height:1200px;overflow:hidden}
body{position:relative;background:var(--white);font-family:"PT Sans",Arial,sans-serif;color:var(--text)}
.abs{position:absolute}

/* header */
.site-header{position:absolute;left:0;top:0;width:966px;height:128px;
  background:repeating-linear-gradient(45deg,var(--header) 0 2px,var(--header-dark) 2px 4px)}
.brand{left:100px;top:28px;font-size:46px;color:var(--white);letter-spacing:-1px;line-height:1}
.contact-item{top:57px;font-size:9px;font-weight:700;color:var(--white);display:flex;align-items:center;gap:6px}
.contact-item .dot{width:11px;height:11px;border-radius:50%;background:var(--red);display:inline-block}
.account-link{top:59px;font-size:9px;font-weight:700;color:#e6e6e6}
.main-nav a{position:absolute;top:105px;height:23px;background:var(--tab);color:#e8e8e8;font-size:10.5px;font-weight:700;text-align:center;line-height:24px;text-decoration:none}
.main-nav a.active{background:var(--red);color:var(--white)}
.star-search{left:708px;top:111px;font-size:10px;font-weight:700;color:var(--white)}
.icon-btn{top:106px;width:22px;height:22px;background:var(--red)}
.cart-badge{left:853px;top:100px;width:12px;height:12px;border-radius:50%;background:var(--white);color:#333;font-size:7px;font-weight:700;text-align:center;line-height:12px}

/* form */
.section-title{height:22px;background:var(--red);color:var(--white);font-size:11.5px;font-weight:700;line-height:22px;padding-left:11px;text-transform:uppercase}
.section-rule{height:1px;background:var(--rule)}
.note{left:100px;top:203px;font-size:8.5px}
.note a{color:var(--red);text-decoration:none}
.field-label{left:121px;font-size:8.5px;color:var(--label)}
.field-label sup{color:var(--red)}
.field{left:242px;width:174px;height:21px;background:var(--field);border:1px solid var(--field-line)}
.select{font-size:7px;color:#999;padding:9px 0 0 17px}
.select .arrow{position:absolute;right:7px;top:5px;width:9px;height:9px;border:1px solid #999;background:#fafafa}
.agree{left:242px;top:760px;font-size:8.5px}
.agree a{color:var(--red);text-decoration:none}
.checkbox{left:419px;top:762px;width:7px;height:7px;border:1px solid #bbb;background:#eee}
.send-btn{left:435px;top:757px;width:61px;height:18px;background:var(--red);color:var(--white);font-size:8px;font-weight:700;text-align:center;line-height:18px}

/* footer */
.site-footer{position:absolute;left:0;top:983px;width:966px;height:172px;background:var(--footer)}
.footer-bar{position:absolute;left:0;top:1155px;width:966px;height:45px;background:var(--footer-bar)}
.footer-head{top:1024px;font-size:8.5px;font-weight:700;color:var(--white);text-transform:uppercase}
.footer-text{top:1041px;font-size:6.5px;line-height:10px;color:var(--footer-text)}
.read-more{font-size:6.5px;color:var(--footer-text)}
.card{top:1077px;width:24px;height:13px;border-radius:2px}
.map-area{left:600px;top:1040px;width:84px;height:70px;border-radius:30% 40% 45% 35%;background:linear-gradient(160deg,#9a9a9a,#7d7d7d)}
.legal{top:1175px;font-size:6.5px;color:#ddd}
.social{top:1168px;width:16px;height:16px;border-radius:50%;background:#e8e8e8}
</style>
</head>
<body>

<header class="site-header">
  <div class="abs brand">plovy</div>
  <div class="abs contact-item" style="left:232px"><span class="dot"></span>+39 0300 55 0100</div>
  <div class="abs contact-item" style="left:330px"><span class="dot"></span>info@plovy.example</div>
  <div class="abs contact-item" style="left:435px"><span class="dot"></span>live chat</div>
  <div class="abs account-link" style="left:587px">my account</div>
  <div class="abs account-link" style="left:642px">my wishlist</div>
  <div class="abs account-link" style="left:696px">log in</div>
  <div class="abs account-link" style="left:745px">create an ads &#8964;</div>
  <div class="abs account-link" style="left:831px">usd &#8964;</div>

  <nav class="main-nav">
    <a class="active" style="left:100px;width:47px">Home</a>
    <a style="left:153px;width:72px">Categories</a>
    <a style="left:235px;width:53px">Buy</a>
    <a style="left:294px;width:53px">Sell</a>
    <a style="left:353px;width:55px">Promos</a>
    <a style="left:414px;width:54px">Ads</a>
    <a style="left:474px;width:53px">Blog</a>
    <a style="left:533px;width:54px">FAQs</a>
    <a style="left:593px;width:54px">Contact</a>
  </nav>
  <div class="abs star-search">Star search</div>
  <div class="abs icon-btn" style="left:809px">
    <svg width="22" height="22" viewBox="0 0 22 22"><circle cx="10" cy="10" r="3.5" fill="none" stroke="#fff" stroke-width="1.3"/><line x1="12.5" y1="12.5" x2="15" y2="15" stroke="#fff" stroke-width="1.5"/></svg>
  </div>
  <div class="abs icon-btn" style="left:838px">
    <svg width="22" height="22" viewBox="0 0 22 22"><path d="M5 8h2l2 6h6l1.5-4.5H8" fill="none" stroke="#fff" stroke-width="1.3"/><circle cx="10" cy="16" r="1" fill="#fff"/><circle cx="14.5" cy="16" r="1" fill="#fff"/></svg>
  </div>
  <div class="abs cart-badge">0</div>
</header>

<main>
  <div class="abs section-title" style="left:100px;top:169px;width:149px">Your personal details</div>
  <div class="abs section-rule" style="left:100px;top:190px;width:765px"></div>
  <p class="abs note">If you already have an account, please login <a href="#">here</a></p>
  <label class="abs field-label" style="top:237px">First Name <sup>*</sup> :</label>
  <div class="abs field" style="top:231px"></div>
  <label class="abs field-label" style="top:270px">Last Name <sup>*</sup> :</label>
  <div class="abs field" style="top:264px"></div>
  <label class="abs field-label" style="top:301px">E Mail :</label>
  <div class="abs field" style="top:296px"></div>

  <div class="abs section-title" style="left:100px;top:346px;width:98px">Your address</div>
  <div class="abs section-rule" style="left:100px;top:367px;width:765px"></div>
  <label class="abs field-label" style="top:398px">Address 1 <sup>?</sup> :</label>
  <div class="abs field" style="top:392px"></div>
  <label class="abs field-label" style="top:431px">Address 2 :</label>
  <div class="abs field" style="top:424px"></div>
  <label class="abs field-label" style="top:462px">City :</label>
  <div class="abs field" style="top:456px"></div>
  <label class="abs field-label" style="top:494px">Post Code :</label>
  <div class="abs field" style="top:488px"></div>
  <label class="abs field-label" style="top:528px">Country :</label>
  <div class="abs field select" style="top:520px">Australy<span class="arrow"></span></div>
  <label class="abs field-label" style="top:558px">Region/State :</label>
  <div class="abs field select" style="top:552px;width:96px">Please Select<span class="arrow"></span></div>

  <div class="abs section-title" style="left:100px;top:603px;width:149px">Your personal details</div>
  <div class="abs section-rule" style="left:100px;top:624px;width:774px"></div>
  <label class="abs field-label" style="top:655px">Password :</label>
  <div class="abs field" style="top:649px"></div>
  <label class="abs field-label" style="top:688px">Password Confirm :</label>
  <div class="abs field" style="top:681px"></div>

  <p class="abs agree">I have read and agree to the <a href="#">Privacy policy</a></p>
  <div class="abs checkbox"></div>
  <div class="abs send-btn">Send Message</div>
</main>

<footer>
  <div class="site-footer"></div>
  <h4 class="abs footer-head" style="left:103px">About us</h4>
  <p class="abs footer-text" style="left:103px;width:90px">Fugit aut illo omnis explicabo ipsa, nemo ipsam quasi dolores voluptatem dolo perspiciatis beatae magni architecto odit</p>
  <span class="abs read-more" style="left:103px;top:1112px">Read more &nbsp;&#8250;</span>

  <h4 class="abs footer-head" style="left:233px">Customer service</h4>
  <p class="abs footer-text" style="left:233px;width:80px">Aut illo omnis odit explicabo ipsa nemo ipsam quasi dolores voluptatem dolo perspiciatis beatae magni architecto</p>
  <span class="abs read-more" style="left:233px;top:1112px">Read more &nbsp;&#8250;</span>

  <h4 class="abs footer-head" style="left:361px">Shipping</h4>
  <p class="abs footer-text" style="left:361px;width:70px">Aseut illo omnis odit explicabo ipsa nemo ipsam quasi dolores voluptatem dolo perspiciatis beatae magni</p>
  <span class="abs read-more" style="left:361px;top:1112px">Read more &nbsp;&#8250;</span>

  <h4 class="abs footer-head" style="left:463px">Payment</h4>
  <p class="abs footer-text" style="left:463px;width:115px">Explicabo ipsa, nemo ipsam quasi dolores voluptatem dolo perspiciatis</p>
  <div class="abs card" style="left:463px;background:#e9e9e9"></div>
  <div class="abs card" style="left:494px;background:#c9c9c9"></div>
  <div class="abs card" style="left:525px;background:#5b8fc4"></div>

  <h4 class="abs footer-head" style="left:607px">Searc by maps</h4>
  <div class="abs map-area" role="img" aria-label="Map of Australia for searching by region"></div>

  <h4 class="abs footer-head" style="left:721px">Top categories</h4>
  <p class="abs footer-text" style="left:721px;width:145px">dolor sit amet • rem eos illo omnis ipsam ipsa • odit aut aperiam • explicabo ipsa unde sed enim • explicabo ipsa accusantium laudantium sunt • perspiciatis ipsam ipsam dolores • totam undes • beatae magni</p>
  <span class="abs read-more" style="left:721px;top:1104px">Read more &nbsp;&#8250;</span>

  <div class="footer-bar"></div>
  <span class="abs legal" style="left:102px">© 2013 <b style="color:#fff">plovy</b></span>
  <span class="abs legal" style="left:171px">About us &nbsp;• Blog &nbsp;• Terms and use &nbsp;• Privacy Policy &nbsp;• Search &nbsp;• Contact us</span>
  <div class="abs social" style="left:720px"></div>
  <div class="abs social" style="left:745px"></div>
  <div class="abs social" style="left:770px"></div>
  <div class="abs social" style="left:794px"></div>
  <div class="abs social" style="left:819px"></div>
  <div class="abs social" style="left:844px"></div>
</footer>

</body>
</html>
```